New Business Cards for Torvin Group

We need a new Business Card to compliment our new logo. We are a vibrant design, manufacture and install business providing recreation areas, public parks and Municipal spaces. We want business cards that are classy, modern and clean.

We have recently changed our logo, and are celebrating our 40th anniversary. We want business cards with a new modern design to reflect our status.

Target Market(s)

Customers

Contact Information for Business Card

We need all the details of our 3 offices as per the business card attached. Please disregard the old logo on the business card, the other three files show our new logo.

Requirements
Must have
• All info as per attached business card but with new logo.
Nice to have

```html
<!DOCTYPE html>
<html lang="en">
<head>
<meta charset="utf-8">
<title>Torvin Group Business Card</title>
<link href="https://fonts.googleapis.com/css2?family=Lato:wght@400;700;900&display=swap" rel="stylesheet">
<style>
  :root {
    --bg: #2a2a2a;
    --card: #ffffff;
    --red: #e8333a;
    --charcoal: #4a4a4e;
    --ink: #333336;
  }
  * { margin: 0; padding: 0; box-sizing: border-box; }
  html, body { width: 1200px; height: 895px; overflow: hidden; background: var(--bg); }
  body { font-family: 'Lato', sans-serif; color: var(--ink); position: relative; }

  .card {
    position: absolute; left: 100px; top: 161px;
    width: 1000px; height: 572px;
    background: var(--card); border-radius: 36px; overflow: hidden;
  }

  .brand { position: absolute; left: 80px; top: 160px; display: flex; align-items: center; gap: 14px; }
  .brand-dot { width: 64px; height: 64px; border-radius: 50%; background: var(--red); flex: none; }
  .brand-name { font-weight: 900; font-size: 38px; letter-spacing: 1px; color: var(--charcoal); line-height: 1; white-space: nowrap; }
  .brand-est { position: absolute; left: 340px; top: 226px; font-size: 21px; color: var(--ink); }

  .person { position: absolute; left: 570px; top: 78px; }
  .person-name { color: var(--red); font-size: 36px; font-weight: 400; line-height: 1; }
  .person-role { font-size: 19px; margin-top: 6px; }
  .person-contacts { margin-top: 22px; font-size: 19px; line-height: 1.35; }
  .contact-line { display: flex; align-items: center; gap: 10px; }
  .contact-line svg { width: 20px; height: 20px; flex: none; }

  .office-bar {
    position: absolute; height: 42px; color: #fff; font-size: 20px;
    display: flex; align-items: center; padding-left: 60px;
  }
  .office-bar.head { left: 0; top: 340px; width: 430px; background: var(--charcoal); }
  .office-bar.qatar { left: 440px; top: 298px; width: 230px; background: var(--red); padding-left: 40px; }
  .office-bar.dubai { left: 680px; top: 256px; width: 320px; background: var(--charcoal); padding-left: 40px; }

  .office-info { position: absolute; font-size: 19px; line-height: 1.25; white-space: nowrap; }
  .office-info.head { left: 60px; top: 392px; }
  .office-info.qatar { left: 480px; top: 350px; }
  .office-info.dubai { left: 720px; top: 308px; }

  .footer-strip { position: absolute; left: 0; bottom: 0; width: 1000px; height: 32px; }

  .footer-link { position: absolute; font-size: 20px; white-space: nowrap; }
  .footer-link .label { color: var(--red); }
  .footer-link.email { left: 300px; top: 492px; }
  .footer-link.web { left: 720px; top: 450px; }
</style>
</head>
<body>
  <div class="card">
    <div class="brand">
      <div class="brand-dot"></div>
      <div class="brand-name">TORVIN GROUP</div>
    </div>
    <div class="brand-est">Est. 1979</div>

    <div class="person">
      <div class="person-name">Samir Haddan</div>
      <div class="person-role">Managing Partner</div>
      <div class="person-contacts">
        <div class="contact-line">
          <svg viewBox="0 0 20 20"><circle cx="10" cy="10" r="10" fill="#e8333a"/><path d="M6.5 5.5l2 0 1 2.5-1.2 1a6 6 0 0 0 2.7 2.7l1-1.2 2.5 1v2a1 1 0 0 1-1 1A8 8 0 0 1 5.5 6.5a1 1 0 0 1 1-1z" fill="#fff"/></svg>
          <span>+971 (0)50 480 7723</span>
        </div>
        <div class="contact-line">
          <svg viewBox="0 0 20 20"><circle cx="10" cy="10" r="10" fill="#e8333a"/><rect x="5" y="6.5" width="10" height="7" rx="1" fill="#fff"/><path d="M5.5 7l4.5 3.5L14.5 7" fill="none" stroke="#e8333a" stroke-width="1.2"/></svg>
          <span>samir@torvingroup.com</span>
        </div>
      </div>
    </div>

    <div class="office-bar head">Head Office</div>
    <div class="office-bar qatar">Qatar Office</div>
    <div class="office-bar dubai">Dubai Office</div>

    <div class="office-info head">
      P.O. Box: 4812 Abu Dhabi<br>U.A.E.<br>Tel: +971 (0)2 5530917<br>Fax: +971 (0)2 5530918
    </div>
    <div class="office-info qatar">
      P.O. Box: 20734 Doha<br>Qatar<br>Tel: +974 44719382<br>Fax: +974 44719383
    </div>
    <div class="office-info dubai">
      P.O. Box: 258146 Dubai<br>U.A.E.<br>Tel: +971 (0)4 3862045<br>Fax: +971 (0)4 3862046
    </div>

    <div class="footer-link email"><span class="label">Email:</span> info@torvingroup.com</div>
    <div class="footer-link web"><span class="label">Web:</span> www.torvingroup.com</div>

    <svg class="footer-strip" viewBox="0 0 1000 32" preserveAspectRatio="none">
      <polygon points="0,0 640,0 660,32 0,32" fill="#4a4a4e"/>
      <polygon points="672,0 1000,0 1000,32 692,32" fill="#4a4a4e"/>
    </svg>
  </div>
</body>
</html>
```